The title of the book is Beyond the Tidewater and the subtitle of the book is Walking Faith Through Rivers

I need a book cover that has a picture of a valley that is between two mountains. The picture needs to show mountains and a valley, not canyons and a valley. The focus should be on the valley. The attached covers are covers that I like with similar book titles. I would like for my name to be in all caps...DR. MARCUS J. HOLLOWAY

Target Market(s)

Religious: Christian: Spiritual: Ages 21 and up

Industry/Entity Type

Religious

Requirements
Must have
• I need to see mountains and a valley, not canyons and valleys. The designer must know the difference between a canyon and a mountain. Looking for a contemporary design.

```html
<!DOCTYPE html>
<html lang="en">
<head>
<meta charset="UTF-8">
<title>Beyond the Tidewater — Cover Spread</title>
<link href="https://fonts.googleapis.com/css2?family=Yellowtail&family=Cinzel:wght@400&family=EB+Garamond:wght@400&display=swap" rel="stylesheet">
<style>
  :root {
    --page-bg: #ececec;
    --paper: #ffffff;
    --ink: #1c1c1c;
    --navy: #1d3a5c;
    --spine-grey: #4a4f55;
    --sky: #e4eef0;
    --meadow: #7fa65a;
    --forest: #2f5236;
    --river: #9fc3cf;
    --rock: #4b545c;
    --white: #ffffff;
  }
  * { margin: 0; padding: 0; box-sizing: border-box; }
  html, body {
    width: 899px; height: 1200px; overflow: hidden;
    background: var(--page-bg);
  }
  .cover-spread {
    position: absolute;
    left: 10px; top: 296px;
    width: 879px; height: 608px;
    background: var(--paper);
    box-shadow: 0 2px 8px rgba(0,0,0,0.25);
    overflow: hidden;
  }
  .landscape-photo {
    position: absolute;
    left: 352px; top: 0;
    width: 527px; height: 608px;
    background: linear-gradient(to bottom,
      var(--sky) 0%, #cfe0dc 14%, #a9c48c 30%, var(--meadow) 40%,
      var(--forest) 55%, #556b63 66%, var(--river) 72%, var(--rock) 82%, #3a4148 100%);
    -webkit-mask-image: linear-gradient(to right, transparent 0%, rgba(0,0,0,0.6) 25%, #000 45%);
    mask-image: linear-gradient(to right, transparent 0%, rgba(0,0,0,0.6) 25%, #000 45%);
  }
  .script-title {
    font-family: 'Yellowtail', cursive;
    color: var(--navy);
    line-height: 0.95;
    text-align: center;
  }
  .back-title {
    position: absolute;
    left: 100px; top: 66px; width: 220px;
    font-size: 38px;
  }
  .back-copy {
    position: absolute;
    left: 38px; top: 152px; width: 330px;
    font-family: 'EB Garamond', serif;
    font-size: 10.6px; line-height: 13.1px;
    color: var(--ink);
    text-align: justify;
  }
  .back-copy p + p { margin-top: 13px; }
  .spine-title, .spine-author {
    position: absolute;
    writing-mode: vertical-rl;
    white-space: nowrap;
  }
  .spine-title {
    left: 438px; top: 118px;
    font-family: 'Yellowtail', cursive;
    font-size: 24px; color: var(--navy);
  }
  .spine-author {
    left: 441px; top: 370px;
    font-family: 'Cinzel', serif;
    font-size: 15px; color: var(--spine-grey);
  }
  .front-title {
    position: absolute;
    left: 500px; top: 42px; width: 360px;
    font-size: 62px;
  }
  .front-subtitle {
    position: absolute;
    left: 500px; top: 180px; width: 360px;
    font-family: 'Cinzel', serif;
    font-size: 15px; color: var(--navy);
    text-align: center; letter-spacing: 0.3px;
  }
  .front-author {
    position: absolute;
    right: 16px; top: 540px;
    font-family: 'Cinzel', serif;
    font-size: 25px; color: var(--white);
    letter-spacing: 0.5px;
  }
</style>
</head>
<body>
  <div class="cover-spread">
    <div class="landscape-photo" role="img" aria-label="Photograph of a green mountain valley with pine forest and a river rushing over grey rocks, fading into white toward the back cover"></div>

    <h2 class="script-title back-title">Beyond the Tidewater</h2>
    <div class="back-copy">
      <p>Lorem ipsum dolor sit amet, consectetur adipiscing elit. Nulla luctus ullamcorper nisi, in sodales dolor tristique nec. Donec molestie, ipsum sed condimentum finibus, eros mauris pellentesque nisl, sit amet accumsan metus est vestibulum mi. Vestibulum ante ipsum primis in faucibus orci luctus et ultrices posuere cubilia curae; Cras in tellus erat. Pellentesque ac urna quam. Donec non velit at lectus commodo aliquet. Orci varius natoque penatibus et magnis dis parturient montes, nascetur ridiculus mus. Nunc nisl tellus, convallis tincidunt velit a, mattis commodo sem. Morbi ac tortor viverra, lobortis nibh a, aliquet tellus. Aenean convallis leo ac imperdiet malesuada. Aliquam vitae enim at nulla porta laoreet. Donec ultrices purus risus, vitae pretium lectus egestas ac. Curabitur dui odio, dictum id metus at, scelerisque hendrerit libero. Nam varius lorem elit, quis tristique lacus sollicitudin mollis. Nulla facilisi. Vivamus nec orci sed lectus pharetra efficitur.</p>
      <p>Ut sollicitudin mauris sapien, id fringilla metus convallis vel. Vivamus ac volutpat metus. Vivamus vehicula id sapien at iaculis. Sed volutpat quam quis nisl tempus, congue luctus metus euismod. Aliquam erat volutpat. Duis placerat posuere pretium. Aenean consectetur id mauris et interdum. Phasellus et leo odio. Proin et enim et metus porta consequat. Pellentesque luctus eget nibh a feugiat. Praesent sollicitudin purus eget sodales blandit. In hac habitasse platea dictumst.</p>
    </div>

    <div class="spine-title">Beyond the Tidewater</div>
    <div class="spine-author">DR. MARCUS J. HOLLOWAY</div>

    <h1 class="script-title front-title">Beyond the<br>Tidewater</h1>
    <div class="front-subtitle">Walking Faith Through Rivers</div>
    <div class="front-author">DR. MARCUS J. HOLLOWAY</div>
  </div>
</body>
</html>
```